Accounting Firm

We are a two partner accounting firm. our business name is BELLWOOD & TRASK. We are accountants and business consultants.

We need a stationery design for our letterhead, with compliments slip, business card and envelope.

We'd like clean, professional look. I'm 39 years old and my partner is 60+, so we'd like modern yet elegant design. Dark Navy Blue as a primary colour is preferred.

Thank you.
Updates

Hi Guys

No logo.

Thanks

Industry/Entity Type

Accounting

Requirements
Must have
• Firm name :BELLWOOD & TRASK
Business Consultants & Accountants
Address: Level 2 Units 3 & 4, 17 Merrow Crescent DALEFORD SA 5099
Box address: PO Box 418 ASHGROVE SA 5098
telp: +61 8 8555 0142
fax: +61 8 8555 0187

Martin Bellwood, CA
Lucas Trask, CPA

martin.bellwood@bellwoodtrask.example.com.au
lucas.trask@bellwoodtrask.example.com.au

Dark Navy Blue as primary colour

```html
<!DOCTYPE html>
<html lang="en">
<head>
<meta charset="utf-8">
<title>Bellwood &amp; Trask – Business Card</title>
<link rel="stylesheet" href="https://fonts.googleapis.com/css2?family=Noto+Serif:ital,wght@0,400;1,400&display=swap">
<style>
  :root {
    --card-bg: #d3e5f6;
    --wedge: #93a9dc;
    --navy: #2a3d69;
    --serif: "Noto Serif", Georgia, serif;
  }
  html, body {
    margin: 0;
    padding: 0;
    overflow: hidden;
    background: #ffffff;
  }
  .card {
    position: relative;
    width: 1200px;
    height: 686px;
    background: var(--card-bg);
    overflow: hidden;
    font-family: var(--serif);
    color: var(--navy);
  }
  .card__wedge {
    position: absolute;
    inset: 0;
    width: 1200px;
    height: 686px;
  }
  .card__wedge polygon { fill: var(--wedge); }

  .firm-name {
    position: absolute;
    left: 50px;
    top: 18px;
    margin: 0;
    font-weight: 400;
    font-size: 84px;
    line-height: 1;
  }
  .firm-name span { display: block; }
  .firm-name__amp {
    font-size: 34px;
    line-height: 1;
    margin: -6px 0 -10px 44px;
  }

  .contact-lines {
    position: absolute;
    right: 40px;
    top: 34px;
    margin: 0;
    text-align: right;
    font-size: 31px;
    line-height: 52px;
  }
  .contact-lines p { margin: 0; }

  .partners {
    position: absolute;
    left: 0;
    width: 1180px;
    top: 290px;
    text-align: center;
  }
  .partners__name {
    margin: 0;
    font-size: 37px;
    line-height: 56px;
  }
  .partners__role {
    margin: 2px 0 0;
    font-style: italic;
    font-size: 23px;
    line-height: 30px;
  }

  .address {
    position: absolute;
    left: 0;
    width: 1180px;
    top: 490px;
    margin: 0;
    text-align: center;
    font-style: normal;
    font-size: 32px;
    line-height: 48px;
  }

  .email {
    position: absolute;
    top: 608px;
    margin: 0;
    font-size: 23px;
    line-height: 32px;
  }
  .email--left { left: 52px; }
  .email--right { right: 40px; }
</style>
</head>
<body>
  <main class="card">
    <svg class="card__wedge" viewBox="0 0 1200 686" aria-hidden="true">
      <polygon points="180,374 1200,56 1200,686 1120,686"/>
    </svg>

    <h1 class="firm-name">
      <span>Bellwood</span>
      <span class="firm-name__amp">&amp;</span>
      <span>Trask</span>
    </h1>

    <div class="contact-lines">
      <p>Tel: +61 8 8555 0142</p>
      <p>Fax: +61 8 8555 0187</p>
    </div>

    <div class="partners">
      <p class="partners__name">Martin Bellwood, CA</p>
      <p class="partners__name">Lucas Trask, CPA</p>
      <p class="partners__role">Business Consultants &amp; Accountants</p>
    </div>

    <address class="address">
      Level 2 Units 3 &amp; 4, 17 Merrow Crescent DALEFORD SA 5099<br>
      PO Box 418 ASHGROVE SA 5098
    </address>

    <p class="email email--left">martin.bellwood@bellwoodtrask.example.com.au</p>
    <p class="email email--right">lucas.trask@bellwoodtrask.example.com.au</p>
  </main>
</body>
</html>
```